Kestrel Summit 2019 Enemies of the End-Times Church Flyer

We want a church conference flyer designed. We are looking for a professional, yet catchy design that uses our brand colors and logo creatively while communicating key information of the event effectively. <br/>The flyer must include all of the following:<br/>Title: Kestrel Summit 2019<br/>Topic: The Enemies of The End-Times Church <br/>Subtitles: <br/> -How the antichrist raises an army by social behavior engineering. <br/>-How the architects of modern social constructs escaped the church's radar. <br/>-The Holy Spirit's end-times agenda:<br/> The Knock-Out Punch!<br/>Speaker: Prophet Marcus Toliver <br/>Dates/time: December 27, 28 & 29 at 6pm<br/>Location: Halvorn Community Center <br/> 241 Pellham Street <br/> Portland, ME 04102<br/>Contact info: phone: 207-555-0148 <br/>email: contact@brookmeadow.example <br/> www.vutel.example<br/>*The flyer must also include a picture of the speaker and our Vutel logo <br/>Thanks, we look forward to seeing what you come up with!

Colors

Designer to choose colors to be used in the design.

Requirements
Must have
• The flyer must include all of the following:
• Title: Kestrel Summit 2019
• Topic: The Enemies of The End-Times Church
• Subtitles:
• -How the antichrist raises an army by social behavior engineering.
• -How the architects of modern social constructs escaped the church's radar.
• -The Holy Spirit's end-times agenda:
• The Knock-Out Punch!
• Speaker: Prophet Marcus Toliver
• Dates/time: December 27, 28 & 29 at 6pm
• Location: Halvorn Community Center
• 241 Pellham Street
• Portland, ME 04102
• Contact info: phone: 207-555-0148
• email: contact@brookmeadow.example
• www.vutel.example
• *The flyer must also include a picture of the speaker and our Vutel logo
Should not have
• Pictures of crosses or church buildings

```html
<!DOCTYPE html>
<html lang="en">
<head>
<meta charset="utf-8">
<title>Kestrel Summit 2019 Flyer</title>
<link href="https://fonts.googleapis.com/css2?family=Montserrat:wght@500;600;700;800&display=swap" rel="stylesheet">
<style>
  :root {
    --page: #0a2a44;
    --navy: #003a63;
    --navy-deep: #0b1a3a;
    --orange: #f39a13;
    --amber: #c86a0c;
    --white: #ffffff;
    --ink: #0d0d12;
  }
  * { margin: 0; padding: 0; box-sizing: border-box; }
  html, body {
    width: 1200px; height: 903px; overflow: hidden;
    background: var(--page);
    font-family: "Montserrat", sans-serif;
  }
  .flyer {
    position: absolute; left: 268px; top: 21px;
    width: 664px; height: 860px;
    background: var(--navy);
    overflow: hidden;
  }
  .speaker-photo {
    position: absolute; left: 0; top: 0; width: 664px; height: 480px;
    background:
      radial-gradient(ellipse 60% 70% at 62% 38%, rgba(150,95,40,0.85), rgba(150,95,40,0) 70%),
      linear-gradient(100deg, #05070d 0%, #14182c 22%, #34406a 38%, #8a5a1c 62%, var(--amber) 82%, #d07a10 100%);
  }
  .speaker-photo::after {
    content: ""; position: absolute; left: 0; bottom: 0; width: 100%; height: 55%;
    background: linear-gradient(90deg, rgba(40,60,150,0.75) 0%, rgba(60,80,160,0.45) 45%, rgba(0,0,0,0) 75%);
  }
  .brand {
    position: absolute; left: 70px; top: 76px;
    display: flex; align-items: center; gap: 10px;
    color: var(--white); font-weight: 600; font-size: 40px; letter-spacing: 1px;
  }
  .brand-dot { width: 14px; height: 14px; border-radius: 50%; background: var(--orange); }
  .event-when {
    position: absolute; right: 55px; top: 43px; text-align: right;
    color: var(--white); font-weight: 700; font-size: 17.5px; line-height: 19.5px;
  }
  .event-where {
    position: absolute; right: 56px; top: 113px; text-align: right;
    color: var(--white); font-weight: 600; font-size: 10px; line-height: 12px; letter-spacing: 0.6px;
  }
  .title-rule {
    position: absolute; left: 70px; top: 277px; width: 41px; height: 7px; background: var(--orange);
  }
  .event-title {
    position: absolute; left: 68px; top: 298px;
    color: var(--white); font-weight: 800; font-size: 46px; line-height: 51px; letter-spacing: 0.5px;
  }
  .speaker-credit {
    position: absolute; left: 458px; top: 413px;
    color: var(--white); font-weight: 600; font-size: 12.5px; line-height: 17px; letter-spacing: 0.6px;
  }
  .topic-band {
    position: absolute; left: 0; top: 480px; width: 664px; height: 97px; background: var(--orange);
  }
  .topic {
    position: absolute; left: 70px; top: 22px;
    color: var(--ink); font-weight: 800; font-size: 24px; line-height: 29px; letter-spacing: 0.4px;
  }
  .session-list {
    position: absolute; left: 70px; top: 614px; width: 500px; list-style: none;
    color: var(--white); font-weight: 600; font-size: 11.5px; line-height: 16px; letter-spacing: 2px;
    text-transform: uppercase;
  }
  .session-list li { position: relative; padding-left: 16px; }
  .session-list li::before {
    content: ""; position: absolute; left: 0; top: 5px;
    width: 5px; height: 5px; border-radius: 50%; background: var(--orange);
  }
  .session-finale {
    position: absolute; left: 86px; top: 707px;
    color: var(--orange); font-weight: 700; font-size: 18.5px;
  }
  .contact {
    position: absolute; left: 86px; top: 780px;
    color: var(--white); font-weight: 600; font-size: 10.5px; line-height: 14px; letter-spacing: 0.8px;
  }
  .contact span { display: inline-block; width: 44px; }
  .website {
    position: absolute; right: 55px; top: 802px;
    color: var(--white); font-weight: 700; font-size: 15px; letter-spacing: 1px;
  }
</style>
</head>
<body>
  <main class="flyer">
    <div class="speaker-photo" role="img" aria-label="Photograph of the speaker preaching with a headset microphone, warm orange light"></div>

    <div class="brand"><span class="brand-dot"></span>Vutel</div>

    <div class="event-when">27, 28 &amp; 29<br>DEC ‘19<br>at 6pm</div>
    <div class="event-where">Halvorn Community Center<br>241 Pellham Street<br>Portland, ME 04102</div>

    <div class="title-rule"></div>
    <h1 class="event-title">KESTREL<br>SUMMIT<br>2019</h1>

    <div class="speaker-credit">Speaker:<br>Prophet Marcus Toliver</div>

    <section class="topic-band">
      <h2 class="topic">THE ENEMIES<br>OF THE END - TIMES CHURCH</h2>
    </section>

    <ul class="session-list">
      <li>How the antichrist raises an army by social behavior engineering.</li>
      <li>How the architects of modern social constructs escaped the church’s radar.</li>
      <li>The Holy Spirit’s end-times agenda</li>
    </ul>
    <p class="session-finale">The Knock-Out Punch!</p>

    <div class="contact">
      Contact info:<br>
      <span>phone</span>: 207-555-0148<br>
      <span>email</span>: contact@brookmeadow.example
    </div>
    <div class="website">www.vutel.example</div>
  </main>
</body>
</html>
```